IMPORTANT- PLEASE READ: Seeking Graphic (NOT a logo!)

**Please note**----This NOT a logo or branding project - we are looking for a specific graphic that conveys our core competency areas. See attached as an example (a very poor quality one but gives you an idea as to what we're looking for!)

**********************************************************************************************
The graphic should help convey the core competency areas (see below) that can extend off branches on a tree (just our idea, we are open to your suggestions).

Our international development program (called FieldSpan) is developing a conceptual model that shows how we support development in agriculture and nutrition through providing what is called “extension services”. Extension is the input into a system (typically education/training or programming) that affects behavior change in people, therefore improving the way they do agriculture or approach nutrition. We also work on a series of cross-cutting areas that influence behavior change and agricultural and nutrition outcomes. More info on our website at www.fieldspan.norvale.edu .

We are seeking assistance in developing a design/graphic that is dynamic, symbolic, and powerful, but also shows the relationships between extension and our major impact areas (primary):

-Agriculture
- Nutrition

and our cross-cutting themes (secondary):

-Climate Change and Environment
-Gender
-Youth
-Policy and Governance
-Capacity Building
-Research and Learning
-Technology

We came up with the idea of a tree, whereby the roots would be extension providing uptake of nutrients for the development of branches, which would be our impact areas and cross-cutting themes. This is only one idea we had and haven’t been able to get a decent graphic design for it. We are also very open to other representations of these relationships. Please note that our website’s color scheme is red/orange, yet agriculture has a green/blue color scheme, when making design choices.Visit our website to get a feel for our brand and work. www.fieldspan.norvale.edu

Please be creative (you don't have to use the tree example!) and we look forwards to seeing what you design!

Target Market(s)

marketing materials for donors, partners and others

Industry/Entity Type

Education

Requirements
Must have
• Must LIST ALL CORE COMPETENCY AREAS (primary and secondary!) See above .
• Same colors as out existing branding platform- See www.fieldspan.norvale.edu
Nice to have
Should not have
• Should NOT be a logo- we are NOT looking for a logo or branding materials. We need a GRAPHIC!!!!

```html
<!DOCTYPE html>
<html lang="en">
<head>
<meta charset="utf-8">
<title>FieldSpan – Extension Competency Tree</title>
<link href="https://fonts.googleapis.com/css2?family=Catamaran:wght@600;700;800&display=swap" rel="stylesheet">
<style>
  :root {
    --bg: #f0f0f0;
    --ink: #2b1608;
    --branch: #6b2147;
    --theme: #8e2c3c;
    --theme-shade: #7a2533;
    --impact: #ec5e24;
    --impact-shade: #c24a1c;
    --white: #ffffff;
  }
  html, body { margin: 0; padding: 0; overflow: hidden; background: var(--bg); }
  .canvas { position: relative; width: 1200px; height: 1200px; overflow: hidden; background: var(--bg); }
  .tree { position: absolute; inset: 0; display: block; }
  .branch { fill: none; stroke: var(--branch); stroke-width: 6; stroke-linejoin: round; }
  .bud { fill: var(--branch); }
  .theme-node { fill: var(--theme); stroke: var(--branch); stroke-width: 7; }
  .impact-node { fill: var(--impact); stroke: var(--branch); stroke-width: 7; }
  .tag { fill: var(--ink); }
  .tag-text { fill: var(--white); font-family: "Catamaran", sans-serif; font-weight: 700; font-size: 22px; letter-spacing: 0.3px; text-anchor: middle; }
  .tag-text.impact { font-size: 31px; font-weight: 800; }
  .tag-text.root { font-size: 58px; font-weight: 800; letter-spacing: 1px; }
  .icon { fill: var(--white); stroke: none; }
  .icon-line { fill: none; stroke: var(--white); stroke-linecap: round; }
  .brand { position: absolute; right: 36px; bottom: 64px; margin: 0; font-family: "Catamaran", sans-serif; font-weight: 800; font-size: 54px; color: var(--impact); letter-spacing: 1px; }
</style>
</head>
<body>
<main class="canvas">
  <svg class="tree" width="1200" height="1200" viewBox="0 0 1500 1500" aria-label="Extension roots feeding Nutrition and Agriculture, with cross-cutting themes branching out">
    <!-- branches -->
    <g class="branches">
      <path class="branch" d="M370 392 L470 490 M440 465 L322 460"/>
      <path class="branch" d="M607 325 L577 465 M585 408 L490 309"/>
      <path class="branch" d="M278 583 L432 583 M385 588 L296 678"/>
      <path class="branch" d="M400 768 L482 672 M455 703 L378 701"/>
      <path class="branch" d="M912 325 L937 465 M925 402 L851 403"/>
      <path class="branch" d="M1220 407 L1058 512 M1118 466 L1095 342"/>
      <path class="branch" d="M1078 582 L1226 582 M1135 580 L1211 535"/>
      <path class="branch" d="M1040 662 L1120 760 M1082 706 L1197 707"/>
      <path class="branch" d="M665 568 L740 635 L740 1290"/>
      <path class="branch" d="M638 650 L678 683 L678 1222 M678 975 L620 1065 L620 1222"/>
      <path class="branch" d="M862 633 L800 672 L800 1222 M805 820 L862 912 L862 1222"/>
      <path class="branch" d="M679 424 L825 557 L828 650 M785 525 L727 569"/>
      <path class="branch" d="M646 1274 L646 1290 M832 1274 L832 1290"/>
    </g>
    <g class="buds">
      <circle class="bud" cx="322" cy="460" r="12"/>
      <circle class="bud" cx="490" cy="309" r="12"/>
      <circle class="bud" cx="296" cy="678" r="12"/>
      <circle class="bud" cx="378" cy="701" r="12"/>
      <circle class="bud" cx="851" cy="403" r="12"/>
      <circle class="bud" cx="1095" cy="342" r="12"/>
      <circle class="bud" cx="1211" cy="535" r="12"/>
      <circle class="bud" cx="1197" cy="707" r="12"/>
      <circle class="bud" cx="679" cy="424" r="12"/>
      <circle class="bud" cx="727" cy="569" r="12"/>
    </g>

    <!-- impact areas -->
    <g class="impact nutrition">
      <circle class="impact-node" cx="547" cy="577" r="113"/>
      <circle class="icon" cx="547" cy="577" r="52"/>
      <circle cx="547" cy="577" r="36" fill="none" stroke="var(--impact)" stroke-width="3"/>
      <rect class="icon" x="473" y="535" width="10" height="90" rx="5"/>
      <path class="icon" d="M468 535 h20 v24 a10 10 0 0 1 -20 0 Z"/>
      <ellipse class="icon" cx="615" cy="553" rx="12" ry="20"/>
      <rect class="icon" x="610" y="560" width="10" height="65" rx="5"/>
    </g>
    <g class="impact agriculture">
      <circle class="impact-node" cx="962" cy="577" r="113"/>
      <rect class="icon" x="960" y="520" width="6" height="132" rx="3"/>
      <ellipse class="icon" cx="963" cy="525" rx="10" ry="22"/>
      <g class="icon">
        <ellipse cx="943" cy="560" rx="20" ry="8" transform="rotate(35 943 560)"/>
        <ellipse cx="983" cy="560" rx="20" ry="8" transform="rotate(-35 983 560)"/>
        <ellipse cx="943" cy="588" rx="20" ry="8" transform="rotate(35 943 588)"/>
        <ellipse cx="983" cy="588" rx="20" ry="8" transform="rotate(-35 983 588)"/>
        <ellipse cx="943" cy="616" rx="20" ry="8" transform="rotate(35 943 616)"/>
        <ellipse cx="983" cy="616" rx="20" ry="8" transform="rotate(-35 983 616)"/>
      </g>
    </g>

    <!-- cross-cutting themes -->
    <g class="theme governance">
      <circle class="theme-node" cx="321" cy="336" r="68"/>
      <path class="icon" d="M283 317 L321 297 L359 317 Z"/>
      <rect class="icon" x="287" y="321" width="68" height="5"/>
      <rect class="icon" x="292" y="330" width="7" height="26"/>
      <rect class="icon" x="307" y="330" width="7" height="26"/>
      <rect class="icon" x="328" y="330" width="7" height="26"/>
      <rect class="icon" x="343" y="330" width="7" height="26"/>
      <rect class="icon" x="284" y="359" width="74" height="6"/>
    </g>
    <g class="theme policy">
      <circle class="theme-node" cx="615" cy="257" r="68"/>
      <rect class="icon" x="596" y="222" width="44" height="22" rx="3" transform="rotate(35 618 233)"/>
      <rect class="icon-line" x="0" y="0" width="0" height="0"/>
      <line class="icon-line" x1="625" y1="248" x2="662" y2="272" stroke-width="7"/>
      <rect class="icon" x="578" y="275" width="58" height="14" rx="6"/>
    </g>
    <g class="theme climate">
      <circle class="theme-node" cx="909" cy="257" r="68"/>
      <circle class="icon" cx="910" cy="270" r="31"/>
      <path d="M892 256 q10 -8 18 2 q-2 12 10 14 q-4 14 -16 14 q-2 -12 -12 -14 Z M926 280 q6 4 2 12" fill="var(--theme)"/>
      <ellipse class="icon" cx="910" cy="222" rx="20" ry="11"/>
    </g>
    <g class="theme capacity">
      <circle class="theme-node" cx="1239" cy="340" r="68"/>
      <path class="icon" d="M1213 318 h18 a9 9 0 1 1 16 0 h18 v18 a9 9 0 1 1 0 16 v18 h-52 v-18 a9 9 0 1 0 0 -16 Z"/>
    </g>
    <g class="theme technology">
      <circle class="theme-node" cx="1294" cy="590" r="68"/>
      <circle class="icon-line" cx="1272" cy="590" r="13" stroke-width="10" stroke-dasharray="6 4"/>
      <circle class="icon-line" cx="1305" cy="567" r="11" stroke-width="9" stroke-dasharray="5 4"/>
      <circle class="icon-line" cx="1305" cy="613" r="11" stroke-width="9" stroke-dasharray="5 4"/>
    </g>
    <g class="theme research">
      <circle class="theme-node" cx="1169" cy="812" r="68"/>
      <circle class="icon" cx="1169" cy="806" r="18"/>
      <rect class="icon" x="1160" y="820" width="18" height="18" rx="3"/>
      <g class="icon-line" stroke-width="5">
        <line x1="1169" y1="766" x2="1169" y2="778"/>
        <line x1="1135" y1="806" x2="1123" y2="806"/>
        <line x1="1203" y1="806" x2="1215" y2="806"/>
        <line x1="1145" y1="782" x2="1137" y2="774"/>
        <line x1="1193" y1="782" x2="1201" y2="774"/>
        <line x1="1145" y1="830" x2="1137" y2="838"/>
        <line x1="1193" y1="830" x2="1201" y2="838"/>
      </g>
    </g>
    <g class="theme gender">
      <circle class="theme-node" cx="207" cy="592" r="68"/>
      <g class="icon-line" stroke-width="5">
        <circle cx="184" cy="585" r="15"/>
        <line x1="184" y1="600" x2="184" y2="622"/>
        <line x1="175" y1="612" x2="193" y2="612"/>
        <circle cx="226" cy="596" r="15"/>
        <line x1="237" y1="585" x2="252" y2="570"/>
        <polyline points="240,570 252,570 252,582"/>
      </g>
    </g>
    <g class="theme youth" role="img" aria-label="Youth icon: a group of young people">
      <circle class="theme-node" cx="348" cy="817" r="68"/>
    </g>

    <!-- labels -->
    <g class="tags">
      <rect class="tag" x="535" y="105" width="167" height="52" rx="7"/>
      <text class="tag-text" x="618" y="139">POLICY</text>
      <rect class="tag" x="810" y="100" width="224" height="73" rx="7"/>
      <text class="tag-text" x="922" y="131">CLIMATE CHANGE</text>
      <text class="tag-text" x="922" y="161">&amp; ENVIRONMENT</text>
      <rect class="tag" x="241" y="194" width="167" height="52" rx="7"/>
      <text class="tag-text" x="324" y="228">GOVERNANCE</text>
      <rect class="tag" x="1155" y="178" width="167" height="72" rx="7"/>
      <text class="tag-text" x="1237" y="206">CAPACITY</text>
      <text class="tag-text" x="1237" y="236">BUILDING</text>
      <rect class="tag" x="1211" y="453" width="167" height="52" rx="7"/>
      <text class="tag-text" x="1294" y="488">TECHNOLOGY</text>
      <rect class="tag" x="1240" y="691" width="167" height="73" rx="7"/>
      <text class="tag-text" x="1324" y="720">RESEARCH &amp;</text>
      <text class="tag-text" x="1328" y="751">LEARNING</text>
      <rect class="tag" x="125" y="451" width="167" height="52" rx="7"/>
      <text class="tag-text" x="206" y="484">GENDER</text>
      <rect class="tag" x="131" y="705" width="167" height="52" rx="7"/>
      <text class="tag-text" x="214" y="739">YOUTH</text>
      <rect class="tag" x="457" y="710" width="205" height="64" rx="8"/>
      <text class="tag-text impact" x="560" y="754">NUTRITION</text>
      <rect class="tag" x="831" y="710" width="231" height="64" rx="8"/>
      <text class="tag-text impact" x="947" y="752">AGRICULTURE</text>
      <rect class="tag" x="563" y="1222" width="166" height="52" rx="7"/>
      <text class="tag-text" x="646" y="1257">EXTENSION</text>
      <rect class="tag" x="749" y="1222" width="167" height="52" rx="7"/>
      <text class="tag-text" x="832" y="1257">EXTENSION</text>
      <rect class="tag" x="526" y="1290" width="431" height="108" rx="10"/>
      <text class="tag-text root" x="747" y="1366">EXTENSION</text>
    </g>
  </svg>
  <p class="brand">FieldSpan</p>
</main>
</body>
</html>
```